Website for Lucent Prose Advisory Group

Please design a website that initially contains four or five pages. This work is for a newly formed consulting company, Lucent Prose Advisory Group, that provides training and individual coaching to help business professionals and lawyers write more effectively and efficiently.

We work in a professional and conservative industry. The website should be simple, crisp, and clean.

I have attached a document that describes the four initial pages for the site: 1) a landing page, 2) a webpage that includes the pictures and bios of our two consultants, 3) a webpage that describes our services, and 4) a webpage that will contain a form that visitors can use to submit questions to us.

I also included the following files:
a. a powerpoint slide with our consultants' pictures and bios; and
b. our recently designed logo (jpg and png files).

Thank you!

```html
<!DOCTYPE html>
<html lang="en">
<head>
<meta charset="utf-8">
<title>Lucent Prose Advisory Group</title>
<link rel="stylesheet" href="https://fonts.googleapis.com/css2?family=Tinos:wght@400;700&family=Poppins:wght@400&display=swap">
<style>
:root{
  --red:#c62a35;
  --red-soft:#d94a53;
  --ink:#1d1d1d;
  --text:#2b2b2b;
  --grey-band:#ebebeb;
  --white:#ffffff;
  --footer:#1e1e20;
  --serif:'Tinos', 'Times New Roman', serif;
  --sans:'Poppins', Arial, sans-serif;
}
*{box-sizing:border-box;margin:0;padding:0}
html,body{width:1200px;height:3490px;overflow:hidden;background:var(--white)}
body{position:relative;font-family:var(--sans);color:var(--text)}
.abs{position:absolute}

/* header */
.site-header{left:0;top:0;width:1200px;height:80px;background:var(--white)}
.brand{left:77px;top:30px;font-family:var(--serif);font-size:20px;color:var(--ink)}
.main-nav{top:30px;left:555px;font-family:var(--serif);font-size:19px}
.main-nav a{position:absolute;white-space:nowrap;color:var(--ink);text-decoration:none}
.main-nav a.active{color:var(--red)}

/* hero */
.hero{left:0;top:80px;width:1200px;height:657px;background:#f4f4f4;overflow:hidden}
.hero-photo{left:406px;top:0;width:794px;height:657px;
  background:
    radial-gradient(ellipse 160px 220px at 62% 45%,rgba(245,245,243,.9) 0%,rgba(245,245,243,0) 100%),
    radial-gradient(ellipse 200px 260px at 40% 55%,rgba(55,52,50,.75) 0%,rgba(55,52,50,0) 100%),
    radial-gradient(ellipse 260px 120px at 80% 80%,rgba(110,100,92,.6) 0%,rgba(110,100,92,0) 100%),
    linear-gradient(90deg,#f4f4f4 0%,rgba(220,216,212,.9) 14%,#c9c3bd 32%,#b9b2aa 60%,#9d958e 85%,#847c75 100%)}
.hero-title{left:75px;top:52px;font-family:var(--serif);font-size:52px;line-height:50px;color:var(--ink);font-weight:400}
.hero-copy{left:75px;top:188px;width:545px;font-size:15px;line-height:27px;color:var(--ink)}
.hero-copy p+p{margin-top:21px}

/* section titles */
.section-title{width:1200px;left:0;text-align:center;font-family:var(--serif);font-size:39px;color:var(--ink);font-weight:400}
.title-rule{left:570px;width:60px;height:2px;background:var(--red)}

/* team */
.member-card{left:183px;width:944px;height:322px;border:2px solid #b3b3b3;background:var(--white)}
.member-photo{left:75px;width:190px;height:190px;border-radius:50%;border:5px solid var(--red);
  background:radial-gradient(circle at 50% 45%,#c9a88f 0%,#9c8a7c 45%,#6f7478 100%)}
.member-name{left:105px;top:28px;font-family:var(--serif);font-size:25px;color:var(--ink)}
.member-role{left:105px;top:64px;font-family:var(--serif);font-size:17px;color:var(--red)}
.member-bio{left:105px;top:98px;width:820px;font-size:12.6px;line-height:21.6px;color:var(--ink)}

/* services */
.services-band{left:0;top:2012px;width:1200px;height:803px;background:var(--grey-band)}
.services-intro{left:0;top:2169px;width:1200px;text-align:center;font-size:15px;line-height:28px;color:var(--ink)}
.corner-accent{background:var(--red)}
.service-card{width:508px;height:226px;background:var(--white)}
.service-card.outlined{border:1px solid var(--red-soft)}
.service-icon{left:34px;top:48px;width:60px;height:60px;border-radius:6px;background:#f3d9db}
.service-title{left:123px;top:44px;font-family:var(--serif);font-weight:700;font-size:20px;color:var(--red)}
.service-text{left:123px;top:82px;width:360px;font-size:15px;line-height:26px;color:var(--ink)}

/* contact */
.contact-band{left:0;top:2815px;width:1200px;height:593px;
  background:linear-gradient(135deg,#d23a45 0%,#c52c37 45%,#d8454f 75%,#c0303a 100%)}
.contact-title{color:var(--white)}
.contact-rule{background:var(--white)}
.field{background:var(--white);font-size:13px;color:var(--ink);padding:0 12px;display:flex;align-items:center}
.field.message{align-items:flex-start;padding-top:14px}
.submit-btn{left:517px;top:3283px;width:164px;height:55px;background:var(--ink);color:var(--white);
  font-family:var(--serif);font-size:20px;display:flex;align-items:center;justify-content:center}

/* footer */
.site-footer{left:0;top:3408px;width:1200px;height:82px;background:var(--footer)}
.footer-brand{left:75px;top:29px;font-family:var(--serif);font-size:20px;color:var(--white)}
.copyright{right:75px;top:34px;font-size:12px;color:var(--white)}
</style>
</head>
<body>

<header class="site-header abs">
  <div class="brand abs">Lucent Prose Advisory Group</div>
  <nav class="main-nav abs">
    <a class="active" style="left:0">Home</a>
    <a style="left:96px">About Us</a>
    <a style="left:221px">Consultants</a>
    <a style="left:364px">Services</a>
    <a style="left:481px">Contact Us</a>
  </nav>
</header>

<section class="hero abs">
  <div class="hero-photo abs" role="img" aria-label="Photo of two professionals talking across a table with a laptop in a bright office"></div>
  <h1 class="hero-title abs">Lucent Prose<br>Advisory Group</h1>
  <div class="hero-copy abs">
    <p>Welcome to Lucent Prose Advisory Group. Our consultants improve the written product of business professionals and lawyers by tailoring our training and coaching to our client’s particular objectives and characteristics. We begin by assessing our client’s culture, the writing requirements and skills of its professionals, and the expectations of its leadership. From there, we tailor our training program and coaching emphases.</p>
    <p>Our individual coaching begins with a focus on the reader.<br>With a precise understanding of a reader’s concerns and motivations, a writer can select the appropriate tone, develop an effective narrative, and sharpen any arguments. By developing these skills, we lead the writer to make the complicated judgments necessary for the most effective written communication. The reader – in law and business – guides the writing. We guide the writer.</p>
  </div>
</section>

<h2 class="section-title abs" style="top:795px">Our team</h2>
<div class="title-rule abs" style="top:848px"></div>

<article class="member-card abs" style="top:899px">
  <div class="member-name abs">Elena Marwood</div>
  <div class="member-role abs">Consultant</div>
  <p class="member-bio abs">Elena Marwood is an Associate Professor and Director of the Academic Enrichment Program at Harborview University School of Law. She has devoted her career in legal education to teaching and counseling students and attorneys, with a focus on developing the fundamental skills to promote success and wellbeing in law school and in the legal profession. Previously, she served as a Professor and Director of Academic Excellence, and most recently as Dean and Associate Dean at Eastbridge Law | Kingsport. She is a former member of the faculty at Calder University Law School, a Visiting Professor at Kingsport College Law School, and a Teaching Fellow at Linwood University. She earned a Bachelor of Arts from Marlow University and a Juris Doctor from Halden University Law School. After graduation, she practiced employment law in Connecticut, New York, and Massachusetts. For the past twenty years, she has served as a consultant and advisor to major law firms and corporations nationwide in designing and presenting professional development training focusing on legal writing and analysis.</p>
</article>
<div class="member-photo abs" style="top:950px" role="img" aria-label="Portrait photo of Elena Marwood"></div>

<article class="member-card abs" style="top:1247px">
  <div class="member-name abs">Daniel Ashby</div>
  <div class="member-role abs">Consultant</div>
  <p class="member-bio abs">Daniel Ashby provides legal and business writing consulting services to businesses, business professionals, law firms, and attorneys. He earned a Bachelor of Arts, cum laude, in English from Ashgrove University, a Master of Fine Arts in creative writing from the Prairie State Writers’ Workshop, and a Juris Doctor, cum laude, from Wexford Law School. At the Prairie State Writers’ Workshop, Daniel served as the poetry editor of The Prairie Review. At Wexford Law School, he served as treasurer and as an editor of the Wexford Law Review. Following graduation from Wexford, Daniel practiced law at Pell &amp; Tamsin L.L.P. (now Pell Ardent) in Washington, D.C., then at Crane, Ellery &amp; Voss, L.L.P. in his hometown of Kansas City, MO. After private practice, he worked in the general counsel’s office of Northgate Insurance Solutions and Brightwell Industrial. Daniel was also dedicated to launching and managing with his sister and mother an ophthalmology practice in North Carolina that provides eye care services to patients at senior living facilities.</p>
</article>
<div class="member-photo abs" style="top:1297px" role="img" aria-label="Portrait photo of Daniel Ashby"></div>

<article class="member-card abs" style="top:1598px">
  <div class="member-name abs">Renata Hale</div>
  <div class="member-role abs">Consultant; Director, Sales &amp; Marketing</div>
  <p class="member-bio abs">Daniel Ashby provides legal and business writing consulting services to businesses, business professionals, law firms, and attorneys. He earned a Bachelor of Arts, cum laude, in English from Ashgrove University, a Master of Fine Arts in creative writing from the Prairie State Writers’ Workshop, and a Juris Doctor, cum laude, from Wexford Law School. At the Prairie State Writers’ Workshop, Daniel served as the poetry editor of The Prairie Review. At Wexford Law School, he served as treasurer and as an editor of the Wexford Law Review. Following graduation from Wexford, Daniel practiced law at Pell &amp; Tamsin L.L.P. (now Pell Ardent) in Washington, D.C., then at Crane, Ellery &amp; Voss, L.L.P. in his hometown of Kansas City, MO. After private practice, he worked in the general counsel’s office of Northgate Insurance Solutions and Brightwell Industrial. Daniel was also dedicated to launching and managing with his sister and mother an ophthalmology practice in North Carolina that provides eye care services to patients at senior living facilities.</p>
</article>
<div class="member-photo abs" style="top:1647px" role="img" aria-label="Portrait photo of Renata Hale"></div>

<section class="services-band abs"></section>
<h2 class="section-title abs" style="top:2075px">Our services</h2>
<div class="title-rule abs" style="top:2130px"></div>
<p class="services-intro abs">The list below presents only a snapshot of our training and coaching options.<br>We develop and customize our services to fit each client.</p>

<div class="corner-accent abs" style="left:74px;top:2258px;width:65px;height:8px"></div>
<div class="corner-accent abs" style="left:74px;top:2258px;width:8px;height:80px"></div>
<div class="service-card outlined abs" style="left:84px;top:2265px">
  <div class="service-icon abs" role="img" aria-label="Icon of a group with a gear and key"></div>
  <div class="service-title abs">Training for large groups</div>
  <p class="service-text abs">We customize our training to large groups (more than approximately eighteen participants) based on our client’s dynamics and writing expectations.</p>
</div>
<div class="service-card abs" style="left:613px;top:2265px">
  <div class="service-icon abs" role="img" aria-label="Icon of two people at a table"></div>
  <div class="service-title abs">Training for small groups</div>
  <p class="service-text abs">A smaller audience, fewer than eighteen participants, allows individuals to more actively participate in these interactive presentations.</p>
</div>
<div class="service-card abs" style="left:82px;top:2513px">
  <div class="service-icon abs" role="img" aria-label="Icon of a presenter at a board"></div>
  <div class="service-title abs">Training with individual coaching</div>
  <p class="service-text abs">After a small or large group training, we meet with each individual participant to provide personal feedback on that professional’s writing, emphasizing the strategies and techniques addressed in the group training.</p>
</div>
<div class="service-card abs" style="left:612px;top:2513px">
  <div class="service-icon abs" role="img" aria-label="Icon of two people sharing ideas"></div>
  <div class="service-title abs" style="top:53px">Individual coaching</div>
  <p class="service-text abs" style="top:91px">We coach individuals based on their written product, focusing on effective writing as well as efficient writing.</p>
</div>
<div class="corner-accent abs" style="left:1119px;top:2662px;width:8px;height:84px"></div>
<div class="corner-accent abs" style="left:1061px;top:2738px;width:66px;height:8px"></div>

<section class="contact-band abs" role="img" aria-label="Red-toned background photo of a person writing at a desk"></section>
<h2 class="section-title contact-title abs" style="top:2877px">Contact us</h2>
<div class="title-rule contact-rule abs" style="top:2930px"></div>

<div class="field abs" style="left:164px;top:2975px;width:430px;height:50px">First name</div>
<div class="field abs" style="left:608px;top:2975px;width:430px;height:50px">Last name</div>
<div class="field abs" style="left:164px;top:3037px;width:430px;height:51px">Company name</div>
<div class="field abs" style="left:608px;top:3037px;width:430px;height:51px">Phone number</div>
<div class="field abs" style="left:164px;top:3102px;width:874px;height:50px">Email</div>
<div class="field message abs" style="left:164px;top:3166px;width:874px;height:102px">Message</div>
<div class="submit-btn abs">Submit</div>

<footer class="site-footer abs">
  <div class="footer-brand abs">Lucent Prose Advisory Group</div>
  <div class="copyright abs">Copyrights© 2024 Company Name All Rights Reserved</div>
</footer>

</body>
</html>
```